Update patient consent forms and contract

Objective
Redesign the existing patient contract information document to create a modern,contempory, and easy-to-understand experience for patients. The updated design should improve readability, accessibility, and overall presentation while maintaining compliance with healthcare and legal requirements.

Key Deliverables

Refreshed visual design and layout
Improved information hierarchy and readability
Modern typography and colour palette aligned with brand guidelines
Clear section headings and navigation
Print-ready and digital versions (PDF)

Include KVE Logo within patient KVE consent to treatment. Ideally this document should be portrait not landscape.
Updates

I would love a front page to be included in the document

```html
<!DOCTYPE html>
<html lang="en">
<head>
<meta charset="utf-8">
<title>Harbour Orthodontics – Patient Documents</title>
<link href="https://fonts.googleapis.com/css2?family=Nunito+Sans:wght@400;600;700;800&display=swap" rel="stylesheet">
<style>
:root{
  --bg:#b4b4b4;
  --paper:#ffffff;
  --blue:#1b9ad6;
  --navy:#1f2a44;
  --ink:#3c3c3c;
  --grey:#8a8a8a;
  --rule:#d4d4d4;
}
*{margin:0;padding:0;box-sizing:border-box}
html,body{width:1200px;height:582px;overflow:hidden}
body{background:var(--bg);font-family:"Nunito Sans",Arial,sans-serif;color:var(--ink);position:relative}
.page{position:absolute;top:86px;width:317px;height:410px;background:var(--paper);box-shadow:2px 3px 6px rgba(0,0,0,.18);overflow:hidden}
.page--retainer{left:101px}
.page--payment{left:442px}
.page--consent{left:782px}

/* brand marks */
.brand{display:flex;align-items:center;gap:4px;font-weight:700;white-space:nowrap}
.brand__dot{width:9px;height:9px;border-radius:50%;background:var(--grey)}
.brand--society{color:var(--grey)}
.brand--practice{color:var(--blue)}
.brand__square{width:9px;height:9px;background:var(--blue)}

/* retainer page */
.retainer__brands{position:absolute;top:33px;left:0;width:100%;display:flex;justify-content:center;gap:30px;font-size:9px}
.retainer__brands .brand__dot,.retainer__brands .brand__square{width:14px;height:14px}
.retainer__title{position:absolute;top:75px;width:100%;text-align:center;color:var(--blue);font-size:12.5px;font-weight:800}
.retainer__body{position:absolute;top:96px;left:24px;width:276px;font-size:6.1px;line-height:11.35px;text-align:justify}
.highlight{color:var(--blue);font-weight:700}

/* shared footer */
.footer{position:absolute;top:353px;left:18px;right:12px;border-top:.6px solid var(--rule);display:grid;grid-template-columns:94px 106px 1fr;font-size:3.7px;line-height:5.6px}
.footer__col{padding:6px 0 0 0}
.footer__col+.footer__col{border-left:.6px solid var(--rule);padding-left:10px}
.footer__title{font-weight:800;color:var(--navy);font-size:4.3px;margin-bottom:2px}
.bank-row{display:grid;grid-template-columns:42px 1fr;margin-bottom:3.2px;font-weight:700;color:var(--navy)}
.bank-row span:first-child{color:var(--blue)}
.info-row{display:flex;align-items:center;gap:4px;margin-bottom:3.2px}
.info-row svg{width:5px;height:5px;flex:none}
.doctor{display:flex;gap:3px;margin-bottom:1.6px;line-height:4.6px}
.doctor svg{width:5px;height:6px;flex:none;margin-top:1px}
.doctor b{color:var(--navy)}

/* payment page */
.payment__head{position:absolute;top:14px;left:18px;right:16px;display:flex;align-items:center;justify-content:space-between}
.payment__title{font-size:11px;font-weight:800;color:var(--navy)}
.payment__brands{display:flex;gap:12px;font-size:6px}
.payment__body{position:absolute;top:37px;left:18px;right:17px;font-size:5.2px;line-height:9.4px}
.payment__thanks{font-weight:700;color:var(--navy);font-size:5.4px;margin-bottom:3px}
.rule{border:0;border-top:.6px solid var(--rule);margin:6px 0 8px}
.rule--dash{border-top-style:dashed}
.section-title{color:var(--blue);font-size:8.6px;font-weight:800;position:relative;margin-left:0}
.section-title::before{content:"";position:absolute;left:-7px;top:5px;width:2px;height:2px;border-radius:50%;background:var(--blue)}
.option{position:relative;margin-top:4px;line-height:7.2px}
.option__label{display:flex;align-items:center;gap:5px;font-weight:700;color:var(--navy);font-size:5.7px;margin-bottom:2px}
.checkbox{width:9px;height:9px;border:.9px solid var(--blue);border-radius:1.5px}
.option__icon{position:absolute;left:130px;top:0;width:26px;height:22px}
.option p{margin-bottom:5px}
.signatures{position:absolute;top:316px;left:0;width:100%;display:flex;justify-content:space-around;font-size:6px;font-weight:700;color:var(--navy)}
.signatures div{border-top:.7px solid var(--navy);width:54px;text-align:center;padding-top:1px}

/* consent page */
.consent__col{position:absolute;top:14px;font-size:2.7px;line-height:4.5px;color:#555;text-align:justify}
.consent__col--left{left:7px;width:147px}
.consent__col--right{left:163px;width:145px;border-left:.5px solid var(--rule);padding-left:5px}
.clause{margin-bottom:5.2px}
.clause h3{font-size:3.6px;line-height:5px;color:var(--blue);font-weight:700}
.clause h3.caps{color:var(--navy);font-weight:800}
.clause p{padding-left:3px}
.consent__brands{display:flex;justify-content:center;gap:14px;font-size:4.6px;margin:6px 0 6px}
.consent__brands .brand__dot,.consent__brands .brand__square{width:7px;height:7px}
.consent__title{text-align:center;color:var(--blue);font-size:6.8px;font-weight:800;display:flex;align-items:center;gap:5px}
.consent__title::before,.consent__title::after{content:"";flex:1;border-top:.5px solid var(--rule)}
.consent__list{list-style:none;margin-top:4px;font-size:4.7px;line-height:6.9px;color:var(--navy);text-align:left}
.consent__list li{border-bottom:.5px dashed #9bb8cf;padding:2px 0 2.5px 3px;position:relative}
.consent__list li::before{content:"";position:absolute;left:-1px;top:5px;width:1.5px;height:1.5px;border-radius:50%;background:var(--blue)}
</style>
</head>
<body>

<!-- Page 1: retainer policy -->
<section class="page page--retainer">
  <div class="retainer__brands">
    <div class="brand brand--society"><span class="brand__dot"></span>KVE</div>
    <div class="brand brand--practice"><span class="brand__square"></span>Harbour Orthodontics</div>
  </div>
  <h1 class="retainer__title">Our retainer policy</h1>
  <p class="retainer__body">Wearing your retainers is the most important part of your orthodontic journey. Teeth shifting is a part of the natural ageing process just like getting wrinkles, so lifetime maintenance is crucial. Healthy teeth are not meant to be glued together, they are individual units and function independently. This is normally only done for areas of weak bone and gum or damaged teeth. For this reason <span class="highlight">WE DO NOT ENCOURAGE THE USE OF ‘BONDED’ OR ‘PERMANENT’ RETAINERS.</span> Instead we advocate responsible use of removable retainers to maintain your smile. Permanent or bonded retainers are not actually permanent and can cause other unexpected problems after treatment is completed, such as difficulty to clean around those teeth which can cause plaque trapping and lead to localised gum and bone loss. They are subject to breaking frequently, which is the reason that when bonded retainers are placed, it is recommended that you still wear a removable retainer over them anyway. Bonded retainers only hold the front few teeth, whereas your orthodontic treatment involved improvements of ALL your teeth. Thus, holding the front teeth only gives the back teeth a chance to move out of alignment. The retainers we provide at Harbour Orthodontics, are only worn at night and will hold ALL your teeth where they are at the end of your orthodontic treatment. Even excellent retainer wear will not guarantee that the teeth will stay exactly the same forever, due to the natural ageing and bone changing processes. Minor alignment adjustments may be made to your retainers in the future to ensure that you remain happy with your smile. After 2 years of retainer reviews, further follow up care may be charged at the current office visit rate. Lost or broken retainers will incur a fee for replacement or repair.</p>

  <footer class="footer">
    <div class="footer__col">
      <div class="footer__title">Our bank account details:</div>
      <div class="bank-row"><span>Account Name</span><span>: Harbour Orthodontics</span></div>
      <div class="bank-row"><span>Bank</span><span>: Coastal Bank</span></div>
      <div class="bank-row"><span>BSB</span><span>: 012 345</span></div>
      <div class="bank-row"><span>Account Number</span><span>: 12345678</span></div>
    </div>
    <div class="footer__col">
      <div class="footer__title">Information:</div>
      <div class="info-row"><svg viewBox="0 0 10 10"><path d="M5 1a3 3 0 0 1 3 3c0 2-3 5-3 5S2 6 2 4a3 3 0 0 1 3-3z" fill="none" stroke="#1b9ad6" stroke-width=".9"/></svg>48 Ridge Rd, Eastfield VIC 3199</div>
      <div class="info-row"><svg viewBox="0 0 10 10"><path d="M2 1.5l2 .3.6 2-1.2.8a5 5 0 0 0 2 2l.8-1.2 2 .6.3 2C6 8.5 1.5 4 2 1.5z" fill="none" stroke="#1b9ad6" stroke-width=".8"/></svg>03 9000 1234</div>
      <div class="info-row"><svg viewBox="0 0 10 10"><rect x="2" y="2" width="6" height="6" fill="none" stroke="#1b9ad6" stroke-width=".8"/><path d="M3.5 4h3M3.5 6h3" stroke="#1b9ad6" stroke-width=".7"/></svg>03 9000 5678</div>
      <div class="info-row"><svg viewBox="0 0 10 10"><rect x="1.5" y="2.5" width="7" height="5" fill="none" stroke="#1b9ad6" stroke-width=".8"/><path d="M1.5 2.5l3.5 3 3.5-3" fill="none" stroke="#1b9ad6" stroke-width=".7"/></svg>hello@harbour-ortho.com.au</div>
    </div>
    <div class="footer__col">
      <div class="footer__title">Registered Specialist Orthodontists:</div>
      <div class="doctor"><svg viewBox="0 0 10 12"><path d="M2 1c2 0 2 1 3 1s1-1 3-1c1.5 0 1.5 3 .5 5L7.5 11 6 7H4l-1.5 4L1.5 6C.5 4 .5 1 2 1z" fill="none" stroke="#1b9ad6" stroke-width=".8"/></svg><div><b>Dr Anna Whitford</b><br>MDSc, Grad Dip Clin Dent, BDSc(Hons)</div></div>
      <div class="doctor"><svg viewBox="0 0 10 12"><path d="M2 1c2 0 2 1 3 1s1-1 3-1c1.5 0 1.5 3 .5 5L7.5 11 6 7H4l-1.5 4L1.5 6C.5 4 .5 1 2 1z" fill="none" stroke="#1b9ad6" stroke-width=".8"/></svg><div><b>Dr Leo Marsh</b><br>MDSc, Grad Dip Clin Dent, MOrth, BDSc</div></div>
      <div class="doctor"><svg viewBox="0 0 10 12"><path d="M2 1c2 0 2 1 3 1s1-1 3-1c1.5 0 1.5 3 .5 5L7.5 11 6 7H4l-1.5 4L1.5 6C.5 4 .5 1 2 1z" fill="none" stroke="#1b9ad6" stroke-width=".8"/></svg><div><b>Dr Owen Reyes</b><br>DCD, MOrth, MRACDS (Orth), BDSc (Hons)</div></div>
    </div>
  </footer>
</section>

<!-- Page 2: payment option selection -->
<section class="page page--payment">
  <header class="payment__head">
    <h1 class="payment__title">Payment Option Selection</h1>
    <div class="payment__brands">
      <div class="brand brand--society"><span class="brand__dot"></span>KVE</div>
      <div class="brand brand--practice"><span class="brand__square"></span>Harbour Orthodontics</div>
    </div>
  </header>
  <div class="payment__body">
    <p class="payment__thanks">Thank you for choosing Harbour Orthodontics.</p>
    <p>To assist with managing your treatment fees, please select your preferred payment method below. If you would prefer to pay at each scheduled appointment, please advise our reception team. Please note that appointments are generally scheduled every 6–8 weeks.</p>
    <hr class="rule">
    <h2 class="section-title">Please select one option:</h2>
    <div class="option">
      <div class="option__label"><span class="checkbox"></span>Credit Card Direct Debit</div>
      <svg class="option__icon" viewBox="0 0 26 22" fill="none" stroke="#8fcbe9" stroke-width=".8"><rect x="1" y="2" width="19" height="13" rx="1"/><path d="M1 6h19M4 10h7"/><circle cx="20" cy="16" r="4"/><path d="M18 16h4l-1.5-1.5"/></svg>
      <p>I would like to pay via credit card direct debit.</p>
      <p>I understand that Harbour Orthodontics will send me a secure PayLink payment link to enter my credit card details. The card provided will be securely stored and used as my nominated payment method for future scheduled payments relating to my treatment plan.</p>
    </div>
    <hr class="rule rule--dash">
    <div class="option">
      <div class="option__label"><span class="checkbox"></span>Monthly Direct Bank Transfer</div>
      <svg class="option__icon" viewBox="0 0 26 22" fill="none" stroke="#8fcbe9" stroke-width=".8"><rect x="2" y="3" width="20" height="18" rx="2"/><path d="M2 8h20M7 1v4M17 1v4M8 12h9l-2-2M17 16H8l2 2"/></svg>
      <p>I would like to pay via monthly direct bank transfer.</p>
      <p>I understand that I am responsible for ensuring monthly payments are made on time in accordance with my agreed payment arrangement.</p>
    </div>
    <hr class="rule">
    <h2 class="section-title">Important</h2>
    <p style="line-height:7.2px">When making direct transfer payments, please use the <b>patient’s full name</b> as the payment reference (for example: Jane Citizen), rather than the account holder’s name. This ensures payments are correctly allocated to your treatment account.</p>
    <h2 class="section-title" style="margin-top:6px">Patient Declaration</h2>
    <p>I have read and understood the payment options above and agree to my selected payment method.</p>
  </div>
  <div class="signatures"><div>Signature</div><div>Date</div></div>

  <footer class="footer">
    <div class="footer__col">
      <div class="footer__title">Our bank account details:</div>
      <div class="bank-row"><span>Account Name</span><span>: Harbour Orthodontics</span></div>
      <div class="bank-row"><span>Bank</span><span>: Coastal Bank</span></div>
      <div class="bank-row"><span>BSB</span><span>: 012 345</span></div>
      <div class="bank-row"><span>Account Number</span><span>: 12345678</span></div>
    </div>
    <div class="footer__col">
      <div class="footer__title">Information:</div>
      <div class="info-row"><svg viewBox="0 0 10 10"><path d="M5 1a3 3 0 0 1 3 3c0 2-3 5-3 5S2 6 2 4a3 3 0 0 1 3-3z" fill="none" stroke="#1b9ad6" stroke-width=".9"/></svg>48 Ridge Rd, Eastfield VIC 3199</div>
      <div class="info-row"><svg viewBox="0 0 10 10"><path d="M2 1.5l2 .3.6 2-1.2.8a5 5 0 0 0 2 2l.8-1.2 2 .6.3 2C6 8.5 1.5 4 2 1.5z" fill="none" stroke="#1b9ad6" stroke-width=".8"/></svg>03 9000 1234</div>
      <div class="info-row"><svg viewBox="0 0 10 10"><rect x="2" y="2" width="6" height="6" fill="none" stroke="#1b9ad6" stroke-width=".8"/><path d="M3.5 4h3M3.5 6h3" stroke="#1b9ad6" stroke-width=".7"/></svg>03 9000 5678</div>
      <div class="info-row"><svg viewBox="0 0 10 10"><rect x="1.5" y="2.5" width="7" height="5" fill="none" stroke="#1b9ad6" stroke-width=".8"/><path d="M1.5 2.5l3.5 3 3.5-3" fill="none" stroke="#1b9ad6" stroke-width=".7"/></svg>hello@harbour-ortho.com.au</div>
    </div>
    <div class="footer__col">
      <div class="footer__title">Registered Specialist Orthodontists:</div>
      <div class="doctor"><svg viewBox="0 0 10 12"><path d="M2 1c2 0 2 1 3 1s1-1 3-1c1.5 0 1.5 3 .5 5L7.5 11 6 7H4l-1.5 4L1.5 6C.5 4 .5 1 2 1z" fill="none" stroke="#1b9ad6" stroke-width=".8"/></svg><div><b>Dr Anna Whitford</b><br>MDSc, Grad Dip Clin Dent, BDSc(Hons)</div></div>
      <div class="doctor"><svg viewBox="0 0 10 12"><path d="M2 1c2 0 2 1 3 1s1-1 3-1c1.5 0 1.5 3 .5 5L7.5 11 6 7H4l-1.5 4L1.5 6C.5 4 .5 1 2 1z" fill="none" stroke="#1b9ad6" stroke-width=".8"/></svg><div><b>Dr Leo Marsh</b><br>MDSc, Grad Dip Clin Dent, MOrth, BDSc</div></div>
      <div class="doctor"><svg viewBox="0 0 10 12"><path d="M2 1c2 0 2 1 3 1s1-1 3-1c1.5 0 1.5 3 .5 5L7.5 11 6 7H4l-1.5 4L1.5 6C.5 4 .5 1 2 1z" fill="none" stroke="#1b9ad6" stroke-width=".8"/></svg><div><b>Dr Owen Reyes</b><br>DCD, MOrth, MRACDS (Orth), BDSc (Hons)</div></div>
    </div>
  </footer>
</section>

<!-- Page 3: treatment information and consent -->
<section class="page page--consent">
  <div class="consent__col consent__col--left">
    <div class="clause"><h3 class="caps">• ORTHODONTIC TREATMENT</h3><p>Orthodontic treatment aims to create a healthy, functional bite and a pleasing smile. Results depend on good care and cooperation from the patient throughout. Please ask your orthodontist to explain any part of your plan you do not fully understand. Like any healing process, outcomes vary and cannot be guaranteed, and each case differs from the next.</p></div>
    <div class="clause"><h3 class="caps">• BENEFITS</h3><p>Treatment helps balance the face and teeth, supports healthy chewing and can improve confidence. Straight teeth are easier to clean, lowering the risk of decay and gum disease. The benefit for each person depends on their own conditions and goals.</p></div>
    <div class="clause"><h3 class="caps">• RISKS</h3><p>All medical and dental care carries some risk. Problems in orthodontics are rare and usually minor, yet you should weigh them when deciding on treatment. The main risks are listed below.</p></div>
    <div class="clause"><h3>1. Oral Hygiene</h3><p>Braces do not cause decay, but poor cleaning and sugary food can leave white marks on teeth. Brush well after every meal and keep regular visits with your dentist during treatment.</p></div>
    <div class="clause"><h3>2. Relapse</h3><p>Teeth may drift after treatment as the face grows and ages. Wearing retainers as advised reduces this. Wisdom teeth, habits and natural change can also affect results, and further treatment may sometimes be needed.</p></div>
    <div class="clause"><h3>3. Periodontal Health</h3><p>Gum and bone health can be affected during treatment, especially where a problem already exists. Daily cleaning and dental checks help keep the gums and supporting bone healthy.</p></div>
    <div class="clause"><h3>4. Root Shortening</h3><p>In some patients root length may shorten during treatment. This is hard to predict and rarely causes problems, but it may affect the long-term life of the teeth.</p></div>
    <div class="clause"><h3>5. Jaw Joints</h3><p>Some patients may notice joint pain, headaches or ear discomfort. These can occur with or without treatment and should be reported to your orthodontist straight away.</p></div>
    <div class="clause"><h3>6. Tooth Vitality</h3><p>A tooth injured in the past or with large fillings may be affected by movement. Rarely, root canal care may be needed to keep the tooth healthy.</p></div>
  </div>

  <div class="consent__col consent__col--right">
    <div class="clause"><h3>7. Loose appliances and discomfort</h3><p>Cheeks and lips may be irritated by new or loose appliances. Tell us about any breakage soon. Mild tenderness after adjustments is normal and usually settles in one to two days.</p></div>
    <div class="clause"><h3>8. Atypical Growth</h3><p>Unusual growth of the jaws may limit results or extend treatment time. In some cases further treatment or surgery may be needed to reach the best outcome.</p></div>
    <div class="clause"><h3>9. Headgear</h3><p>Headgear can cause injury if handled poorly. Remove it during rough play or sport.</p></div>
    <div class="clause"><h3>10. Treatment Time</h3><p>Treatment may take longer than estimated if appliances are not worn, hygiene is poor or appointments are missed, which can also affect results.</p></div>
    <div class="clause"><h3>11. Co-operation</h3><p>Your cooperation is the best way to achieve a good result. Without it, the plan may need to change or treatment may be stopped early.</p></div>
    <div class="clause"><h3>12. Ceramic Brackets</h3><p>Ceramic brackets may rarely chip or wear opposing teeth. Small pieces may break on removal and care is taken to protect the enamel.</p></div>
    <div class="clause"><h3>13. Complementary aesthetic dentistry</h3><p>Where teeth differ in size or shape, extra work such as bonding, crowns or gum care may be needed to complete your smile.</p></div>
    <div class="clause"><h3>14. General Health</h3><p>General health can affect treatment. Please let your orthodontist know of any change to your health.</p></div>

    <div class="consent__brands">
      <div class="brand brand--society"><span class="brand__dot"></span>KVE</div>
      <div class="brand brand--practice"><span class="brand__square"></span>Harbour Orthodontics</div>
    </div>
    <h2 class="consent__title">CONSENT TO TREATMENT</h2>
    <ul class="consent__list">
      <li>I here by authorize:</li>
      <li>To carry out orthodontic treatment and any other related procedures deemed necessary including X-rays, for the welfare and treatment of:</li>
      <li>Signature of patient or parent/guardian:</li>
      <li>Name :</li>
      <li>Relationship to patient :</li>
      <li>Date :</li>
      <li>Signature of Orthodontis :</li>
    </ul>
  </div>
</section>

</body>
</html>
```